Set up small scale company website

We need a website set up for our educational consultancy - Brellin Learning. We like the following site and want something similar www.quorvadeplan.co.uk We can provide the copy and images but need the following:- setting up the overall theme and design - to our requirements on colours and forma- Approximately 4 pages of services offered and with an index pageEtct (yellow and green)And the following pages - as well as a home page:- A contact page linked to our email addresses and registered business address 17 Millbrook Lane, Harwich, Essex, CO12 5JP- About Us page - An index of services page that links to between 4-6 pages outlining services- A News page that links to updates of latest services, events and activities - easily updated by usOn the homepage we'd like links to twitter and LinkedIn feeds and links to our other blogs and websites
Target Market(s)
Schools, local authoroties and multi-academy trusts
Logo Text
Brellin Learning
Coding
Coded - Design and coding required
Number of Pages Required
5+ page
Font styles to use
Requirements
Should not have
- No tacky pictures of mortar boards or chalk boards etc.

```html
<!DOCTYPE html>
<html lang="en">
<head>
<meta charset="utf-8">
<title>Brellin Learning</title>
<link href="https://fonts.googleapis.com/css2?family=Poppins:wght@400;500;600&display=swap" rel="stylesheet">
<style>
:root{--green:#8cb518;--yellow:#f5e41c;--dark:#1d1e20;--band:#4b4e53;--ink:#333;--muted:#8a8a8a;--light:#f4f4f4;--line:#e3e3e3}
*{margin:0;padding:0;box-sizing:border-box}
html,body{width:1200px;height:1200px;overflow:hidden;background:#fff;font-family:'Poppins',sans-serif}
.stage{position:absolute;left:0;top:0;width:1500px;height:1500px;transform:scale(.8);transform-origin:0 0}
.site{position:absolute;left:505px;top:0;width:492px;height:1500px;background:#fff;overflow:hidden}
.abs{position:absolute}
.t{position:absolute;font-size:4px;line-height:1.6;color:var(--muted)}
.topbar{left:0;top:0;width:492px;height:16px;background:var(--green)}
.topbar .dot{position:absolute;top:5px;width:6px;height:6px;border-radius:50%;background:rgba(255,255,255,.8)}
.topbar .t{color:#fff;top:4px;font-size:4.5px}
.logo{left:61px;top:27px;font-size:9px;font-weight:600;color:var(--green)}
.nav{left:172px;top:32px;font-size:4.5px;color:var(--green);display:flex;gap:13px}
.hero{left:0;top:54px;width:492px;height:265px;background:linear-gradient(100deg,#1c2420 0%,#2e3a33 45%,#6a6257 70%,#3a3a36 100%)}
.hero h1{position:absolute;left:61px;top:50px;font-weight:400;font-size:17px;line-height:20px;color:#fff}
.hero h1 span{color:var(--yellow)}
.btn{position:absolute;background:var(--yellow);color:#333;font-size:4.5px;font-weight:600;text-align:center}
.arrow{position:absolute;width:15px;height:15px;background:var(--green)}
.events{left:61px;top:254px;width:369px;height:65px;background:#fff}
.events .strip{position:absolute;left:0;top:0;width:21px;height:65px;background:var(--green)}
.ev-date{position:absolute;font-size:7px;font-weight:600;color:var(--green);text-align:center;width:12px;line-height:7px}
.ev-date small{display:block;font-size:3.5px;color:var(--muted);font-weight:400}
.h2{position:absolute;left:0;width:492px;text-align:center;font-size:10px;font-weight:500;color:var(--ink)}
.dots{position:absolute;left:241px;width:10px;height:2px;background:radial-gradient(circle,var(--green) 0.8px,transparent 1px) 0 0/3.4px 2px}
.sub{position:absolute;left:170px;width:152px;text-align:center;font-size:4px;line-height:1.6;color:var(--muted)}
.photo{position:absolute}
.svc{position:absolute;width:88px;text-align:center}
.svc .ic{width:36px;height:36px;margin:0 auto;border-radius:50%;border:1px solid var(--line);background:#fff;display:flex;align-items:center;justify-content:center}
.svc .ic.on{background:var(--green);border:3px solid #d7e8a8}
.svc b{display:block;margin-top:9px;font-size:6px;font-weight:500;color:var(--ink)}
.svc p{font-size:4px;line-height:1.6;color:var(--muted);margin-top:6px}
.news{left:0;top:693px;width:492px;height:178px;background:var(--band)}
.news .t{color:#ddd}
.quote{left:0;top:896px;width:492px;height:90px;background:var(--light)}
.card{position:absolute;top:1069px;width:106px;height:160px;background:#fff;box-shadow:0 1px 4px rgba(0,0,0,.15)}
.card b{position:absolute;left:7px;top:76px;font-size:5px;font-weight:500;color:var(--green)}
.field{position:absolute;border:1px solid var(--line);font-size:3.5px;color:#aaa;padding:3px}
.footer{left:0;top:1355px;width:492px;height:145px;background:var(--dark)}
.footer .t{color:#999}
.footer h4{position:absolute;top:24px;font-size:6px;font-weight:500;color:#fff}
.thumb{position:absolute;width:18px;height:16px;background:linear-gradient(135deg,#a98a6e,#5c4a3f)}
</style>
</head>
<body>
<div class="stage"><div class="site">

<div class="abs topbar">
  <span class="dot" style="left:66px"></span><span class="dot" style="left:80px"></span><span class="dot" style="left:94px"></span>
  <svg class="abs" style="left:297px;top:5px" width="6" height="6" viewBox="0 0 10 10"><path d="M2 1l2 2-1 1.5c1 1.5 2 2.5 3.5 3.5L8 6.5l2 2-1.5 1.5C4.5 9.5.5 5.5 0 2.5z" fill="#fff"/></svg>
  <span class="t" style="left:306px">01632 400512</span>
  <svg class="abs" style="left:349px;top:5px" width="7" height="5" viewBox="0 0 14 10"><rect x="0.5" y="0.5" width="13" height="9" fill="none" stroke="#fff"/><path d="M.5.5l6.5 5 6.5-5" fill="none" stroke="#fff"/></svg>
  <span class="t" style="left:358px">hello@brellinlearning.co.uk</span>
</div>

<div class="abs logo">Brellin Learning</div>
<nav class="abs nav"><span>Home</span><span>About Us</span><span>News</span><span>Blog</span><span>Services</span><span>Contact Us</span></nav>
<svg class="abs" style="left:424px;top:32px" width="7" height="7" viewBox="0 0 10 10"><circle cx="4" cy="4" r="3" fill="none" stroke="#333" stroke-width="1.4"/><path d="M6.2 6.2L9 9" stroke="#333" stroke-width="1.4"/></svg>

<section class="abs hero" role="img" aria-label="Photo of a smiling student holding notebooks in a library">
  <h1><span>set up for our</span><br>educational consultancy</h1>
  <p class="t" style="left:61px;top:97px;width:165px;color:#fff">What a refreshing approach Quorvade Ltd has. Their approach to supporting schools is modern</p>
  <div class="btn" style="left:61px;top:126px;width:63px;height:20px;line-height:20px">GET IN TOUCH</div>
  <div class="arrow" style="left:415px;top:116px"><svg width="15" height="15"><path d="M6 4l4 3.5-4 3.5" fill="none" stroke="#fff"/></svg></div>
  <div class="arrow" style="left:415px;top:134px;background:#4c5f20"><svg width="15" height="15"><path d="M9 4l-4 3.5 4 3.5" fill="none" stroke="#fff"/></svg></div>
</section>

<div class="abs events">
  <div class="strip"><span class="abs" style="left:4px;top:52px;transform:rotate(-90deg);transform-origin:0 0;font-size:4.5px;color:#fff;white-space:nowrap">LATEST EVENTS</span></div>
  <div class="ev-date" style="left:47px;top:12px">29<small>JUN</small></div>
  <div class="ev-date" style="left:47px;top:38px">15<small>OCT</small></div>
  <div class="ev-date" style="left:192px;top:12px">16<small>JUN</small></div>
  <div class="ev-date" style="left:192px;top:38px">20<small>NOV</small></div>
  <span class="t" style="left:70px;top:11px;width:105px">The following feedback was received from delegates who attended.</span>
  <span class="t" style="left:70px;top:37px;width:105px">The following feedback was received from delegates who attended.</span>
  <span class="t" style="left:214px;top:11px;width:115px">This has inspired me to achieve and move into the role of Quorvade in more depth"</span>
  <span class="t" style="left:214px;top:37px;width:115px">This has inspired me to achieve and move into the role of Quorvade in more depth"</span>
  <span class="abs" style="left:348px;top:0;width:21px;height:65px;background:#f6f6f6"></span>
</div>

<div class="h2" style="top:341px">About Us</div><div class="dots" style="top:356px"></div>
<p class="sub" style="top:363px">We provide high quality, professional and affordable finance and business services to schools and academies.</p>
<div class="photo" style="left:65px;top:394px;width:161px;height:78px;background:linear-gradient(120deg,#e9eef2,#b7cbe0 50%,#d8b9a6)" role="img" aria-label="Photo of a teacher with pupils in a classroom"></div>
<p class="t" style="left:242px;top:397px;width:185px">Quorvade Ltd provides high quality and affordable business and accountancy services to schools and academies. All our services are managed and delivered by an energetic team who has a wealth of experience, a range of business management qualifications and an excellent reputation in the education arena. We have a national team of experts who will work</p>
<p class="t" style="left:242px;top:439px;width:185px">collaboratively with your own staff to ensure our services are tailored to meet your specific needs and budget with our focus always on saving you time and money.</p>
<span class="t" style="left:242px;top:463px;color:var(--green)">Read More...</span>

<div class="h2" style="top:496px">Services</div><div class="dots" style="top:511px"></div>
<p class="sub" style="top:518px">We provide high quality, professional and affordable finance and business services to schools and academies.</p>
<div class="svc" style="left:60px;top:558px"><div class="ic"><svg width="16" height="16" viewBox="0 0 16 16"><rect x="5" y="2" width="10" height="7" fill="none" stroke="#8cb518"/><circle cx="3" cy="5" r="1.5" fill="#8cb518"/><path d="M2 7h2v7M3 9l4-2" stroke="#8cb518" fill="none"/></svg></div><b>Training &amp; Events</b><p>With the ever changing landscape of school business management</p></div>
<div class="svc" style="left:155px;top:558px"><div class="ic on"><svg width="16" height="16" viewBox="0 0 16 16"><circle cx="8" cy="3" r="2" fill="#fff"/><circle cx="3" cy="12" r="2" fill="#fff"/><circle cx="13" cy="12" r="2" fill="#fff"/><path d="M8 5v4M3 10V9h10v1" stroke="#fff" fill="none"/></svg></div><b>Finance</b><p>Schools have a statutory obligation to accurately account for public</p></div>
<div class="svc" style="left:250px;top:558px"><div class="ic"><svg width="16" height="16" viewBox="0 0 16 16"><circle cx="8" cy="4" r="2.5" fill="#8cb518"/><rect x="4" y="8" width="8" height="3" fill="#8cb518"/><rect x="2" y="12" width="12" height="2" fill="#8cb518"/></svg></div><b>Personnel</b><p>Organisations are only as good as their workforce. Well managed and</p></div>
<div class="svc" style="left:345px;top:558px"><div class="ic"><svg width="16" height="16" viewBox="0 0 16 16"><path d="M3 13l6-6M9 7l3-4 2 2-4 3z" stroke="#8cb518" stroke-width="1.5" fill="none"/><circle cx="5" cy="6" r="1.5" fill="#8cb518"/></svg></div><b>Auditing</b><p>Schools have a responsibility to demonstrate effective governance</p></div>
<div class="btn" style="left:216px;top:650px;width:59px;height:18px;line-height:18px">READ MORE</div>

<section class="abs news">
  <div class="abs" style="left:222px;top:0;width:270px;height:178px;background:linear-gradient(90deg,#3b3d41,#5a5d62)" role="img" aria-label="Faded background photo of a woman studying"></div>
  <span class="abs" style="left:61px;top:35px;font-size:6.5px;font-weight:500;color:#fff">NEWS</span>
  <div class="photo" style="left:61px;top:48px;width:161px;height:92px;background:linear-gradient(135deg,#6f8a7a,#c9c3b8 60%,#8b8477)" role="img" aria-label="Photo of a woman working on a laptop in an office"></div>
  <span class="abs" style="left:75px;top:127px;font-size:4.5px;color:#fff">Spring Term Business &amp; Professional Development</span>
  <div class="photo" style="left:223px;top:48px;width:103px;height:52px;background:linear-gradient(135deg,#d9a95a,#8a6b4c 60%,#5a6f88)" role="img" aria-label="Photo of students walking with books"></div>
  <div class="photo" style="left:327px;top:48px;width:103px;height:52px;background:linear-gradient(135deg,#c4c4c4,#7f7b78 60%,#a0938a)" role="img" aria-label="Photo of two people reviewing documents"></div>
  <span class="t" style="left:225px;top:107px;color:var(--yellow)">Celebrating 5 years of Brellin Learning</span>
  <span class="t" style="left:225px;top:117px;width:98px">Lisa Marner (Head of Studies) are pleased &amp; Professional Development</span>
  <span class="t" style="left:225px;top:135px;color:var(--yellow)">Read More..</span>
  <span class="t" style="left:329px;top:107px;color:var(--yellow)">Celebrating 5 years of Brellin Learning</span>
  <span class="t" style="left:329px;top:117px;width:100px">Lisa Marner (Head of Studies) are pleased to &amp; Professional Development event</span>
  <span class="t" style="left:329px;top:135px;color:var(--yellow)">Read More..</span>
</section>

<section class="abs quote">
  <svg class="abs" style="left:60px;top:41px" width="5" height="8"><path d="M4 1L1 4l3 3" fill="none" stroke="#8cb518"/></svg>
  <svg class="abs" style="left:426px;top:41px" width="5" height="8"><path d="M1 1l3 3-3 3" fill="none" stroke="#8cb518"/></svg>
  <div class="abs" style="left:83px;top:22px;width:46px;height:46px;border-radius:50%;background:linear-gradient(135deg,#d8d8d8,#6d6d6d)" role="img" aria-label="Portrait photo of the client quoted"></div>
  <span class="abs" style="left:140px;top:20px;font-size:10px;color:#bbb">”</span>
  <p class="t" style="left:148px;top:28px;width:260px;font-size:4.5px;color:#555">Quorvade Ltd provides high quality and affordable business and accountancy services to schools and academies. All our services are managed and delivered by an energetic team who has a wealth of exp</p>
  <span class="t" style="left:148px;top:58px;color:var(--green);font-style:italic">- Dana Merrow</span>
</section>

<div class="h2" style="top:1008px">Latest Blog</div><div class="dots" style="top:1023px"></div>
<p class="sub" style="top:1030px">We provide high quality, professional and affordable finance and business services to schools and academies.</p>
<div class="card" style="left:73px"><div class="photo" style="left:0;top:0;width:106px;height:65px;background:linear-gradient(135deg,#c0504a,#6b4a3f 60%,#3e4f6e)" role="img" aria-label="Photo of students reading together"></div><b>consultancy - Brellin Learning</b><p class="t" style="left:7px;top:88px;width:92px">To support schools in ensuring they are compliant with data protection legislation, Quorvade is offering a range of support services aimed to meet differing requirements.</p><span class="t" style="left:7px;top:130px">◦ 5 minutes ago</span></div>
<div class="card" style="left:193px"><div class="photo" style="left:0;top:0;width:106px;height:65px;background:linear-gradient(135deg,#e8e4dc,#9ab0c4 60%,#c9a77e)" role="img" aria-label="Photo of pupils drawing at a table"></div><b>consultancy - Brellin Learning</b><p class="t" style="left:7px;top:88px;width:92px">To support schools in ensuring they are compliant with data protection legislation, Quorvade is offering a range of support services aimed to meet differing requirements.</p><span class="t" style="left:7px;top:130px">◦ 5 minutes ago</span></div>
<div class="card" style="left:313px"><div class="photo" style="left:0;top:0;width:106px;height:65px;background:linear-gradient(135deg,#b45a4a,#7f8fa8 60%,#d4c2a8)" role="img" aria-label="Photo of a student studying in a library"></div><b>consultancy - Brellin Learning</b><p class="t" style="left:7px;top:88px;width:92px">To support schools in ensuring they are compliant with data protection legislation, Quorvade is offering a range of support services aimed to meet differing requirements.</p><span class="t" style="left:7px;top:130px">◦ 5 minutes ago</span></div>

<span class="abs" style="left:61px;top:1250px;font-size:10px;font-weight:500;color:var(--ink)">Contact Us</span>
<div class="dots" style="left:61px;top:1268px"></div>
<svg class="abs" style="left:61px;top:1286px" width="5" height="6" viewBox="0 0 10 12"><path d="M5 12C1 7 0 5.5 0 4a5 5 0 0110 0c0 1.5-1 3-5 8z" fill="#8cb518"/></svg>
<span class="t" style="left:69px;top:1285px;width:75px;color:#555">17 Millbrook Lane, Alderwick, Holbury, AW4 5JP</span>
<svg class="abs" style="left:61px;top:1310px" width="5" height="5" viewBox="0 0 10 10"><path d="M2 1l2 2-1 1.5c1 1.5 2 2.5 3.5 3.5L8 6.5l2 2-1.5 1.5C4.5 9.5.5 5.5 0 2.5z" fill="#8cb518"/></svg>
<span class="t" style="left:69px;top:1309px;color:#555">01632 400512</span>
<svg class="abs" style="left:61px;top:1327px" width="6" height="4" viewBox="0 0 12 8"><rect width="12" height="8" fill="#8cb518"/></svg>
<span class="t" style="left:69px;top:1325px;color:#555">hello@brellinlearning.co.uk</span>
<div class="field" style="left:157px;top:1254px;width:84px;height:14px">Your Name</div>
<div class="field" style="left:251px;top:1254px;width:84px;height:14px">Email</div>
<div class="field" style="left:346px;top:1254px;width:84px;height:14px">Subject</div>
<div class="field" style="left:157px;top:1276px;width:273px;height:37px">Message</div>
<div class="btn" style="left:157px;top:1320px;width:63px;height:13px;line-height:13px;background:var(--green);color:#fff">SUBMIT A MESSAGE</div>

<footer class="abs footer">
  <span class="abs" style="left:61px;top:20px;font-size:9px;font-weight:600;color:#fff">Brellin Learning</span>
  <p class="t" style="left:61px;top:42px;width:85px">Brellin Learning provides high quality and affordable business and accountancy services to schools and academies. All our services are managed and delivered by an energetic team who has a wealth of experience in a range of business</p>
  <h4 style="left:159px">Latest News</h4>
  <div class="thumb" style="left:159px;top:48px"></div><span class="t" style="left:185px;top:47px;width:55px">With a flexible portfolio of services<br><span style="color:#ccc">APRIL 1, 2018</span></span>
  <div class="thumb" style="left:159px;top:76px"></div><span class="t" style="left:185px;top:75px;width:55px">With a flexible portfolio of services<br><span style="color:#ccc">APRIL 1, 2018</span></span>
  <h4 style="left:255px">Our Twitter</h4>
  <span class="t" style="left:265px;top:47px;width:72px">I truly cannot remember ever attending a course that news.brellinlearning.co.uk<br><span style="color:var(--green)">10 Days ago</span></span>
  <span class="t" style="left:265px;top:80px;width:72px">I truly cannot remember ever attending a course that news.brellinlearning.co.uk<br><span style="color:var(--green)">26 Days ago</span></span>
  <h4 style="left:353px">Subscribe</h4>
  <div class="field" style="left:353px;top:50px;width:77px;height:14px;border-color:#555;color:#ccc">Email</div>
  <div class="btn" style="left:353px;top:68px;width:77px;height:14px;line-height:14px;background:var(--green);color:#fff">SUBSCRIBE</div>
  <p class="t" style="left:353px;top:88px;width:80px">We offer an extensive range of business management</p>
  <span class="abs" style="left:0;top:130px;width:492px;height:1px;background:#333"></span>
  <span class="t" style="left:61px;top:133px">©2019 Brellin Learning All Rights Reserved</span>
  <span class="abs" style="left:393px;top:135px;width:4px;height:4px;border-radius:50%;background:#aaa"></span>
  <span class="abs" style="left:403px;top:135px;width:4px;height:4px;border-radius:50%;background:#aaa"></span>
  <span class="abs" style="left:413px;top:135px;width:4px;height:4px;border-radius:50%;background:#aaa"></span>
  <span class="abs" style="left:423px;top:135px;width:4px;height:4px;border-radius:50%;background:#aaa"></span>
</footer>

</div></div>
</body>
</html>
```